Popular Australian based wellbeing and high performance podcast needs a design

I need a new, fresh design for my Keep Rising Bright podcast image. This podcast helps and enables its listeners to do their life even better by enhancing their wellbeing, mindset, happiness and leadership. I would love to see designs that include the colour blue. The final design should communicate optimism, hope, approachability and credibility.

Target Market(s)

Target is teenagers to adults wanting to enhance their wellbeing, mindset and happiness.

Font styles to use
Other font styles liked:
• Proba Pro

Colors
33a6d7
0592cd
ffffff

Requirements
Must have
• Must include: Keep Rising Bright podcast
Nice to have
• Could include: with Miles Tervick.

```html
<!DOCTYPE html>
<html lang="en">
<head>
<meta charset="utf-8">
<title>Keep Rising Bright with Miles Tervick</title>
<link rel="stylesheet" href="https://fonts.googleapis.com/css2?family=Lato:wght@400;700&display=swap">
<style>
  :root {
    --deep-blue: #0559a5;
    --brand-blue: #0592cd;
    --sky-blue: #33a6d7;
    --stroke-blue: #8fd3f4;
    --stroke-light: #bfe6f8;
    --pale-sky: #bfe6f8;
    --mist: #eef8fd;
    --shirt-grey: #b9ccd8;
    --white: #ffffff;
  }
  html, body {
    margin: 0;
    padding: 0;
    width: 1200px;
    height: 1173px;
    overflow: hidden;
    background: var(--white);
  }
  .cover {
    position: absolute;
    left: 34px;
    top: 24px;
    width: 1123px;
    height: 1124px;
    background: var(--white);
    box-shadow: 0 6px 18px rgba(0, 0, 0, 0.28);
    overflow: hidden;
    font-family: "Lato", "Gill Sans", sans-serif;
  }
  .top-rule {
    position: absolute;
    left: 0; top: 0;
    width: 100%; height: 27px;
    background: linear-gradient(90deg, var(--deep-blue), var(--brand-blue));
  }
  .backdrop {
    position: absolute;
    left: 0; top: 27px;
    width: 100%; height: 777px;
  }
  .backdrop svg { display: block; }
  .title-band {
    position: absolute;
    left: 0; top: 804px;
    width: 100%; height: 196px;
    background: linear-gradient(90deg, var(--deep-blue) 0%, #0a6db8 60%, var(--brand-blue) 100%);
  }
  .title-band svg, .host-strip svg { display: block; }
  .show-title {
    font-family: "Lato", "Gill Sans", sans-serif;
    font-weight: 700;
    font-size: 146px;
    fill: var(--white);
    filter: drop-shadow(2px 3px 3px rgba(0, 0, 0, 0.35));
  }
  .host-strip {
    position: absolute;
    left: 0; top: 1000px;
    width: 100%; height: 124px;
    background: linear-gradient(90deg, var(--white) 0%, var(--mist) 45%, var(--pale-sky) 100%);
  }
  .host-with {
    font-family: "Lato", "Gill Sans", sans-serif;
    font-size: 50px;
    font-weight: 400;
    fill: var(--deep-blue);
  }
  .host-name {
    font-family: "Lato", "Gill Sans", sans-serif;
    font-size: 90px;
    font-weight: 400;
    fill: var(--deep-blue);
  }
</style>
</head>
<body>
  <main class="cover">
    <div class="top-rule"></div>

    <div class="backdrop">
      <svg width="1123" height="777" viewBox="0 0 1123 777">
        <defs>
          <linearGradient id="strokeFill" x1="0" y1="0" x2="1" y2="1">
            <stop offset="0" stop-color="var(--stroke-blue)"/>
            <stop offset="0.6" stop-color="#a5dcf6"/>
            <stop offset="1" stop-color="var(--stroke-light)"/>
          </linearGradient>
          <linearGradient id="photoFill" x1="0" y1="0" x2="0" y2="1">
            <stop offset="0" stop-color="#c6d9e4"/>
            <stop offset="0.55" stop-color="var(--shirt-grey)"/>
            <stop offset="1" stop-color="#7f97a8"/>
          </linearGradient>
        </defs>
        <rect class="sky-wash" width="1123" height="777" fill="#f6fbfe"/>
        <polygon class="brush-band" fill="url(#strokeFill)"
          points="20,170 300,135 500,140 700,120 880,85 1090,25 1123,20 1123,777 0,777 0,230"/>
        <polygon class="brush-band-lower" fill="#cdeefb"
          points="1123,560 1123,777 700,777"/>
        <path class="host-photo" role="img"
          aria-label="Photo of the smiling host in a grey T-shirt, sitting with arms resting on his knee"
          fill="url(#photoFill)"
          d="M140,777 L140,620 Q150,540 240,500 L330,430 Q380,400 440,395 L440,170 Q450,60 560,50 Q690,50 700,170 L700,390 Q780,400 840,430 Q950,520 945,640 L945,777 Z"/>
      </svg>
    </div>

    <section class="title-band">
      <svg width="1123" height="196" viewBox="0 0 1123 196">
        <text class="show-title" x="561" y="151" text-anchor="middle" textLength="996" lengthAdjust="spacingAndGlyphs">KEEP RISING BRIGHT</text>
      </svg>
    </section>

    <footer class="host-strip">
      <svg width="1123" height="124" viewBox="0 0 1123 124">
        <text x="68" y="84"><tspan class="host-with">with</tspan><tspan class="host-name" dx="8">Miles Tervick</tspan></text>
      </svg>
    </footer>
  </main>
</body>
</html>
```